I need a SEO-friendly Wordpress website (making sure to style H1, H2, H3, etc correctly) for a Hawaii-based law firm called Meridian Crest Legal Group. Comparable websites include https://trvlaw.example/ and https://www.boultem.example/ for design reference. The current copy on the WelbyCounsel.example website can be used.

Coding

```html
<!DOCTYPE html>
<html lang="en">
<head>
<meta charset="utf-8">
<title>Meridian Crest Legal Group — Divorce and Personal Injury Lawyers</title>
<link href="https://fonts.googleapis.com/css2?family=Montserrat:wght@500;600;700;800&family=Open+Sans:wght@400;600&display=swap" rel="stylesheet">
<style>
:root{
  --brand:#b4610f;
  --brand-dark:#5c3006;
  --ink:#222222;
  --text:#555555;
  --muted:#f3f3f3;
  --white:#ffffff;
}
*{margin:0;padding:0;box-sizing:border-box}
html,body{width:1200px;height:4812px;overflow:hidden}
body{position:relative;background:var(--white);font-family:'Open Sans',sans-serif;color:var(--text)}
.abs{position:absolute}
.topbar{left:0;top:0;width:1200px;height:42px;background:var(--brand);color:var(--white)}
.topbar .phone{left:90px;top:10px;font:700 18px 'Montserrat',sans-serif;display:flex;align-items:center;gap:12px}
.topbar .social{right:90px;top:10px;display:flex;gap:6px}
.topbar .social span{width:22px;height:22px;border-radius:50%;background:var(--white);display:block}
.header{left:0;top:42px;width:1200px;height:93px;background:var(--white);border-bottom:1px solid #e5e5e5}
.brand{left:88px;top:26px}
.brand .name{font:700 21px 'Montserrat',sans-serif;color:var(--brand)}
.brand .tag{font-size:12px;color:#444;margin-top:2px}
.nav{right:88px;top:38px;display:flex;gap:36px;font:500 14px 'Montserrat',sans-serif;color:#333}
.hero{left:0;top:135px;width:1200px;height:583px;background:linear-gradient(100deg,#3b3633 0%,#6e655d 45%,#a59b90 70%,#5a524b 100%)}
.hero h1{left:88px;top:120px;font:800 53px/1.22 'Montserrat',sans-serif;color:var(--white)}
.hero p{left:90px;top:268px;font-size:28px;line-height:1.15;color:var(--white)}
.btn-hero{left:90px;top:373px;width:271px;height:75px;background:var(--brand);padding:6px}
.btn-hero span{display:flex;height:100%;border:2px solid var(--white);align-items:center;justify-content:center;color:var(--white);font:600 26px 'Montserrat',sans-serif}
.dots{left:562px;top:537px;display:flex;gap:10px}
.dots span{width:16px;height:16px;border-radius:50%;border:2px solid var(--white)}
.dots span.on{background:var(--white)}
.eyebrow{font:500 26px 'Montserrat',sans-serif;color:var(--brand);display:flex;align-items:center;justify-content:center;gap:18px;width:1200px;left:0}
.eyebrow i{display:block;width:156px;border-top:2px dotted #999}
.h2{left:0;width:1200px;text-align:center;font:800 38px 'Montserrat',sans-serif;color:var(--ink)}
.about-text{left:90px;top:928px;width:542px;font-size:17px;line-height:32.3px;text-align:justify}
.about-img{left:677px;top:938px;width:433px;height:408px;background:linear-gradient(160deg,#d8d2ca,#8c7258 55%,#3d2a1b)}
.btn-box{background:var(--brand);padding:5px}
.btn-box span{display:flex;height:100%;border:2px solid var(--white);align-items:center;justify-content:center;color:var(--white);font:600 16px 'Montserrat',sans-serif}
.team{left:0;top:1421px;width:1200px;height:622px;background:var(--muted)}
.member{top:1611px;width:237px}
.member .photo{height:234px;background:linear-gradient(180deg,#bcbcbc,#3a3a3a)}
.member .name{text-align:center;font:500 17px 'Montserrat',sans-serif;color:#222;margin-top:18px}
.member.active{background:var(--white);box-shadow:0 2px 8px rgba(0,0,0,.15);padding-bottom:12px}
.member.active .name{color:var(--brand);margin-top:14px}
.contact-box{left:174px;top:2150px;width:843px;height:224px;border:2px solid #999}
.tab{background:var(--brand);padding:4px}
.tab span{display:flex;height:100%;border:2px solid var(--white);align-items:center;justify-content:center;color:var(--white);font:700 20px 'Montserrat',sans-serif}
.contact-box h3{position:absolute;left:0;top:68px;width:100%;text-align:center;font:800 25px 'Montserrat',sans-serif;color:var(--ink)}
.contact-box p{position:absolute;left:0;width:100%;text-align:center;font-size:16px;color:#333}
.contact-box b{color:var(--brand)}
.areas-intro{left:200px;top:2530px;width:800px;text-align:center;font-size:17px;line-height:31px;color:#444}
.area-h{font:800 38px 'Montserrat',sans-serif;color:var(--brand)}
.row{left:0;width:1200px;height:417px}
.row .img{position:absolute;top:0;width:604px;height:417px}
.row .copy{position:absolute;top:70px;width:428px}
.row h3{font:700 25px 'Montserrat',sans-serif;color:var(--brand);margin-bottom:22px}
.row p{font-size:14px;line-height:27px;text-align:justify;color:#555}
.hex{position:absolute;left:558px;top:162px;width:88px;height:88px}
.footnav{left:0;top:4332px;width:1200px;height:80px;background:var(--brand);display:flex;justify-content:center;align-items:center;gap:50px;font:700 17px 'Montserrat',sans-serif;color:var(--white)}
.map{left:0;top:4412px;width:1200px;height:350px;background:linear-gradient(135deg,#e8e6e1,#d9dcd6 50%,#e4e2dc)}
.info-card{left:108px;top:4487px;width:337px;height:179px;background:var(--white);box-shadow:0 2px 10px rgba(0,0,0,.2);padding:28px 22px}
.info-card h4{font:700 16px 'Montserrat',sans-serif;color:var(--brand);margin-bottom:12px}
.info-card li{list-style:none;display:flex;gap:16px;font-size:14px;line-height:20px;color:#333;margin-bottom:8px}
.info-card svg{flex:none;margin-top:3px}
.copyright{left:0;top:4762px;width:1200px;height:50px;background:var(--brand-dark);color:var(--white);text-align:center;line-height:50px;font-size:16px}
</style>
</head>
<body>

<div class="abs topbar">
  <div class="abs phone">
    <svg width="18" height="18" viewBox="0 0 24 24"><path fill="#fff" d="M6.6 10.8a15 15 0 0 0 6.6 6.6l2.2-2.2c.3-.3.7-.4 1-.2 1.1.4 2.3.6 3.6.6.6 0 1 .4 1 1V20c0 .6-.4 1-1 1A17 17 0 0 1 3 4c0-.6.4-1 1-1h3.5c.6 0 1 .4 1 1 0 1.3.2 2.5.6 3.6.1.3 0 .7-.2 1z"/></svg>
    +1.808.555.0142
  </div>
  <div class="abs social"><span></span><span></span><span></span><span></span><span></span></div>
</div>

<header class="abs header">
  <div class="abs brand">
    <div class="name">MERIDIAN CREST LEGAL GROUP</div>
    <div class="tag">Divorce and Personal Injury Lawyers</div>
  </div>
  <nav class="abs nav"><span>HOME</span><span>PRACTICE AREAS</span><span>ATTORNEYS</span><span>BLOG</span><span>CONTACT US</span></nav>
</header>

<section class="abs hero" role="img" aria-label="Close-up of hands signing legal documents with a pen">
  <h1 class="abs">MERIDIAN CREST<br>LEGAL GROUP</h1>
  <p class="abs">Dedicated to making sure you receive<br>the care and attention you need.</p>
  <div class="abs btn-hero"><span>GET A STARTED</span></div>
  <div class="abs dots"><span></span><span class="on"></span><span></span></div>
</section>

<div class="abs eyebrow" style="top:797px"><i></i>ABOUT US<i></i></div>
<h2 class="abs h2" style="top:843px">KONA LAWYERS OF MCLG</h2>
<p class="abs about-text">The experienced attorneys in the Meridian Crest Legal Group's Kailua Kona, Hawaii office provide clients with a wide range of litigation expertise, including legal claims involving divorce &amp; family, personal injury, toxic exposures, intellectual property, and real estate.Our Kona office also offers commercial and hospitality litigation expertise on behalf of a wide variety of clients, including restaurants, hotels, property owners, and many others.We never wish to see our clients go to court, though if there is no other option, you're in safe hands with our seasoned trial lawyers and the many years of courtroom experience behind them.</p>
<div class="abs about-img" role="img" aria-label="Judge's gavel on a desk beside a lawyer working on a laptop"></div>
<div class="abs btn-box" style="left:90px;top:1277px;width:179px;height:67px"><span>LEARN MORE</span></div>

<section class="abs team"></section>
<div class="abs eyebrow" style="top:1462px"><i></i>MEET&nbsp; THE&nbsp; TEAM<i></i></div>
<h2 class="abs h2" style="top:1508px">ATTORNEYS OF KONA-BASED MCLG</h2>
<div class="abs member" style="left:90px"><div class="photo" role="img" aria-label="Portrait of attorney Warren Ashby"></div><div class="name">WARREN ASHBY</div></div>
<div class="abs member active" style="left:351px"><div class="photo" role="img" aria-label="Portrait of attorney Daniel Whitlock"></div><div class="name">DANIEL WHITLOCK</div></div>
<div class="abs member" style="left:613px"><div class="photo" role="img" aria-label="Portrait of attorney Thomas R. Kellan"></div><div class="name">THOMAS R. KELLAN</div></div>
<div class="abs member" style="left:874px"><div class="photo" role="img" aria-label="Portrait of attorney Owen P. Marsh"></div><div class="name">OWEN P. MARSH</div></div>
<div class="abs btn-box" style="left:482px;top:1931px;width:238px;height:67px"><span>VIEW ALL ATTORNEYS</span></div>

<div class="abs contact-box">
  <h3>CONTACT MERIDIAN CREST LEGAL GROUP</h3>
  <p style="top:112px">Dedicated to making sure you receive the care and attention you need.</p>
  <p style="top:137px">Contact us today at &nbsp;<b>(1.808.555.0142)</b></p>
</div>
<div class="abs tab" style="left:458px;top:2127px;width:271px;height:48px"><span>CONTACT US</span></div>
<div class="abs tab" style="left:461px;top:2342px;width:266px;height:47px"><span style="font-size:16px;font-weight:600">GET A FREE CONSULTATION</span></div>

<h2 class="abs area-h" style="left:0;width:1200px;text-align:center;top:2464px">AREAS OF PRACTICE</h2>
<p class="abs areas-intro">The Big Island based attorneys of Welby Counsel are licensed in several states, and specialize in numerous areas including divorce, family &amp; custody, personal injury, wrongful death, real estate, contract, and intellectual property.</p>

<section class="abs row" style="top:2664px;background:var(--muted)">
  <div class="img" style="left:0;background:linear-gradient(120deg,#e9e6e2,#b9b2aa 50%,#4e4a47)" role="img" aria-label="Couple in distress removing a wedding ring"></div>
  <div class="copy" style="left:667px"><h3>FAMILY &amp; DIVORCE</h3><p>MCLG's Kona-based lawyers are committed to providing quality and aggressive legal services that minimize the emotional and financial burdens of the legal process for family law clients. Warren Ashby and the entire MCLG legal team takes great pride in the personal attention given to each of client, and it is with this level of caring and our dedication to seeking the most cost effective method for helping you to achieve your goals. Clients benefit from our extensive experience.</p></div>
  <svg class="hex" viewBox="0 0 88 88"><polygon points="22,6 66,6 88,44 66,82 22,82 0,44" fill="#b4610f"/><rect x="28" y="28" width="32" height="32" rx="3" fill="none" stroke="#fff" stroke-width="2.5"/></svg>
</section>

<section class="abs row" style="top:3081px;background:var(--muted)">
  <div class="copy" style="left:88px"><h3>PERSONAL INJURY</h3><p>MCLG's Kona Lawyers are well-versed in torts law and have expertise in all aspects of personal injury including medical malpractice, accidental collisions, product liability, wrongful death, or workplace injury. We always protect our client's interests while making best efforts to have cases settled out of court to save on overall cost.We understand the ins and outs of car accident claims and can use our experience to give you the representation you deserve.</p></div>
  <div class="img" style="left:604px;width:596px;background:linear-gradient(135deg,#3a2416,#8a5a33 50%,#2b1a10)" role="img" aria-label="Gavel, stethoscope and caduceus on law books"></div>
  <svg class="hex" viewBox="0 0 88 88"><polygon points="22,6 66,6 88,44 66,82 22,82 0,44" fill="#b4610f"/><circle cx="44" cy="36" r="9" fill="none" stroke="#fff" stroke-width="2.5"/><path d="M29 62c2-10 28-10 30 0" fill="none" stroke="#fff" stroke-width="2.5"/></svg>
</section>

<section class="abs row" style="top:3498px;background:var(--muted)">
  <div class="img" style="left:0;background:linear-gradient(120deg,#f1eeea,#b9a68f 55%,#4a3a2c)" role="img" aria-label="Business contract being signed beside scales of justice"></div>
  <div class="copy" style="left:667px"><h3>CORPORATE &amp; IP</h3><p>MCLG's Hawaii corporate clients include restaurants, hotels, property owners, and many other types of organizations. Business litigation include dispute in the context of business - both with 3rd parties and within the company itself. Business disputes can arise during the start up of a company, during its operation or when a business is winding down;. Best practices include putting the necessary contracts and agreementsinto place form the outset to minimize litigation.</p></div>
  <svg class="hex" viewBox="0 0 88 88"><polygon points="22,6 66,6 88,44 66,82 22,82 0,44" fill="#b4610f"/><circle cx="44" cy="44" r="16" fill="none" stroke="#fff" stroke-width="2.5"/><line x1="36" y1="44" x2="52" y2="44" stroke="#fff" stroke-width="2.5"/></svg>
</section>

<section class="abs row" style="top:3915px;background:var(--muted)">
  <div class="copy" style="left:88px"><h3>REAL ESTATE</h3><p>Meridian Crest Legal Group has its roots firmlhy planted in real estate. We are, at our core, a real estate law firm. Warren Ashby is also a licensed real estate broker in both Hawaii and California., so we know the law and the business of real estate. We have decades of experience in handling easements grants and disputes, deposit disputes, non-disclosure agreements, sale/purchase contracts</p></div>
  <div class="img" style="left:604px;width:596px;background:linear-gradient(135deg,#e6ddd0,#9a7a58 50%,#3e2818)" role="img" aria-label="Gavel and scales beside a small model house"></div>
  <svg class="hex" viewBox="0 0 88 88"><polygon points="22,6 66,6 88,44 66,82 22,82 0,44" fill="#b4610f"/><path d="M28 46 44 31 60 46M33 42v16h22V42" fill="none" stroke="#fff" stroke-width="2.5"/></svg>
</section>

<nav class="abs footnav"><span>HOME</span><span>PRACTICE AREAS</span><span>ATTORNEYS</span><span>BLOG</span><span>CONTACT US</span></nav>

<div class="abs map" role="img" aria-label="Street map of Kailua Kona showing the office location"></div>
<div class="abs info-card">
  <h4>CONATCT INFO</h4>
  <ul>
    <li><svg width="12" height="14" viewBox="0 0 12 16"><path fill="#b4610f" d="M6 0a6 6 0 0 0-6 6c0 4.5 6 10 6 10s6-5.5 6-10a6 6 0 0 0-6-6zm0 8.5A2.5 2.5 0 1 1 6 3.5a2.5 2.5 0 0 1 0 5z"/></svg><span>4410 Harborline Drive, Suite 210<br>Kailua Kona, Hawaii 96740</span></li>
    <li><svg width="12" height="12" viewBox="0 0 24 24"><path fill="#b4610f" d="M6.6 10.8a15 15 0 0 0 6.6 6.6l2.2-2.2c.3-.3.7-.4 1-.2 1.1.4 2.3.6 3.6.6.6 0 1 .4 1 1V20c0 .6-.4 1-1 1A17 17 0 0 1 3 4c0-.6.4-1 1-1h3.5c.6 0 1 .4 1 1 0 1.3.2 2.5.6 3.6.1.3 0 .7-.2 1z"/></svg><span>+1.808.555.0142</span></li>
    <li><svg width="12" height="12" viewBox="0 0 24 18"><rect width="24" height="18" rx="2" fill="#b4610f"/><path d="M1 2l11 8 11-8" fill="none" stroke="#fff" stroke-width="2"/></svg><span>clients@welbycounsel.example</span></li>
  </ul>
</div>

<footer class="abs copyright">Copyright © Meridian Crest Legal Group. All Rights Reserved.</footer>

</body>
</html>
```